Business card design needed

We are a unique and exciting Drama, Dance and Fitness studio that offers classes from 18 months to adults - with a strong focus on the Under 5's market and we mainly cater for children under 14 years. We aim to create confidence in ALL of our students. We have a very happy and encouraging environment at our studio so would like my business card to 'project this'. I would like my 'catchphrase' - "Building Brave Hearts" - It's your turn to GLOW! to be on the front of my business card also.

Myself as the Principal has a VERY bubbly personality - so I need this business card to project this also. Stars(silver?) and perhaps pictures/silouettes of happy children would be appropriate. And as we also have adult fitness classes, pictures/silouettes of adults in yoga poses/exercise poses would be nice to have too. We are a very 'theatrical' school so would like my business card to look as 'exciting' as possible - but incorporating my school colours of red, royal blue, silver and white.
Updates

                                       

Hi everyone - thankyou so far for your designs.  I feel like I need to show a bit more 'excitement' with the business cards that I have seen so far.  I would definitely like to see stars(preferably silver) on there, and preferably pictures/silhouettes of children happy/performing.  If you can fit pictures/silouettes of adults exercising - yoga/zumba etc that would be a bonus.  I have got an extremely bubbly, theatrical personality, so I need that to be reflected with my name and title on the card also. The colour scheme of my colours red, royal blue, silver and white is a priority too and most of you have done this.  Thankyou.                                   

Target Market(s)

Families with children - especially those who love to perform, and for adults who like to exercise.

Industry/Entity Type

Environment

Contact Information for Business Card

Marisol's Footlight Flyers - Drama Dance Performance and Fitness Studio. Unit 4, 58 Larkspur Rd WATTLEBROOK CENTRAL. "Building Brave Hearts" - It's your turn to GLOW! Marisol Venkley PRINCIPAL. Phone: 0427 395160 Email: brightkids@pelnet.com.au Web: www.marisolsfootlightflyers.com.au

Requirements
Must have
• Our studio colours are Red, Royal Blue with a bit of silver and white. I also LOVE stars - and this would suit my business card. Also need to have my logo on there - which I have uploaded. I would like my 'catchphrase' - "Building Brave Hearts" - It's your turn to GLOW! to be on the front of my business card also.
Nice to have
• Pictures/silouettes of happy children would be appropriate. And as we also have adult fitness classes, pictures/silouettes of adults in yoga poses/exercise poses would be nice to have too. We are a very 'theatrical' school so would like my business card to look as 'exciting' as possible - but incorporating my school colours of red, royal blue, silver and white.

```html
<!DOCTYPE html>
<html lang="en">
<head>
<meta charset="utf-8">
<title>Marisol's Footlight Flyers – Business Card</title>
<link rel="stylesheet" href="https://fonts.googleapis.com/css2?family=Questrial&family=Titillium+Web:ital,wght@1,700&display=swap">
<style>
  :root {
    --red: #ec1c24;
    --royal: #2e3192;
    --navy-text: #2b3a8e;
    --white: #ffffff;
    --backdrop: #e9e7e4;
    --purple: #7b3f98;
    --orange: #f7941d;
    --sky: #1ba1e2;
    --lime: #8dc63f;
    --pink: #ec4b9c;
    --magenta: #c2389a;
  }
  * { margin: 0; padding: 0; box-sizing: border-box; }
  html, body { width: 1200px; height: 900px; overflow: hidden; }
  body { background: var(--backdrop); position: relative; font-family: "Questrial", Arial, sans-serif; }

  .card { position: absolute; left: 248px; width: 704px; background: var(--white); overflow: hidden; box-shadow: 0 2px 8px rgba(0,0,0,.18); }
  .card--back { top: 18px; height: 428px; }
  .card--front { top: 460px; height: 430px; }
  .swoosh { position: absolute; left: 0; top: 0; width: 704px; height: 170px; }

  .brand { position: absolute; color: var(--royal); white-space: nowrap; text-align: center; }
  .brand__name { display: block; }
  .brand__tag { display: block; color: var(--navy-text); }
  .card--back .brand { left: 38px; top: 80px; width: 310px; }
  .card--back .brand__name { font-size: 29px; }
  .card--back .brand__tag { font-size: 11.5px; margin-top: 20px; }
  .card--front .brand { left: 226px; top: 94px; width: 450px; }
  .card--front .brand__name { font-size: 40px; }
  .card--front .brand__tag { font-size: 16px; margin-top: 36px; }

  .contact { position: absolute; left: 41px; top: 180px; color: var(--navy-text); font-size: 14px; line-height: 20px; letter-spacing: .6px; font-style: normal; }
  .contact__address { margin-bottom: 16px; }
  .person { position: absolute; left: 406px; top: 192px; }
  .person__name { color: var(--red); font-size: 23px; letter-spacing: .3px; }
  .person__title { color: var(--navy-text); font-size: 14px; letter-spacing: 3px; margin-top: 4px; }

  .figure { position: absolute; border-radius: 40% 40% 18% 18%; opacity: .85; }
  .figure--purple { background: var(--purple); }
  .figure--orange { background: var(--orange); }
  .figure--sky { background: var(--sky); }
  .figure--lime { background: var(--lime); }
  .figure--pink { background: var(--pink); }
  .figure--dancer { background: linear-gradient(180deg, var(--magenta), var(--purple)); }

  .slogan { position: absolute; left: 0; bottom: 0; width: 704px; height: 68px; background: var(--red); color: var(--white); font-family: "Titillium Web", Arial, sans-serif; font-style: italic; font-weight: 700; font-size: 29px; display: flex; align-items: center; justify-content: center; letter-spacing: .3px; white-space: nowrap; }
</style>
</head>
<body>

<section class="card card--back">
  <svg class="swoosh" viewBox="0 0 704 170" aria-hidden="true">
    <defs>
      <linearGradient id="silverBack" x1="0" x2="1">
        <stop offset="0" stop-color="#a7a9ac"/><stop offset=".5" stop-color="#f2f2f4"/><stop offset="1" stop-color="#a7a9ac"/>
      </linearGradient>
    </defs>
    <path d="M0 0H704V112C600 52 450 18 320 22C190 26 70 52 0 78Z" fill="var(--red)"/>
    <path d="M320 22C470 18 620 60 704 98V122C620 84 470 34 320 22Z" fill="var(--royal)"/>
    <path d="M0 74C120 36 300 14 420 24C520 34 600 80 660 140" fill="none" stroke="url(#silverBack)" stroke-width="10"/>
  </svg>
  <div class="brand">
    <span class="brand__name">Marisol's Footlight Flyers</span>
    <span class="brand__tag">Drama Dance Performance and Fitness Studio</span>
  </div>
  <address class="contact">
    <div class="contact__address">Unit 4, 58 Larkspur Rd<br>WATTLEBROOK CENTRAL</div>
    <div>P: 0427 395160</div>
    <div>E: brightkids@pelnet.com.au</div>
    <div>W: marisolsfootlightflyers.com.au</div>
  </address>
  <div class="person">
    <div class="person__name">Marisol Venkley</div>
    <div class="person__title">PRINCIPAL</div>
  </div>
  <div class="figure figure--purple" style="left:52px;top:320px;width:84px;height:96px" role="img" aria-label="Purple silhouette of a child doing a cartwheel"></div>
  <div class="figure figure--orange" style="left:186px;top:326px;width:88px;height:92px" role="img" aria-label="Orange silhouette of a child star-jumping"></div>
  <div class="figure figure--sky" style="left:326px;top:314px;width:76px;height:106px" role="img" aria-label="Blue silhouette of a child leaping"></div>
  <div class="figure figure--lime" style="left:446px;top:316px;width:72px;height:104px" role="img" aria-label="Green silhouette of a child dancing"></div>
  <div class="figure figure--pink" style="left:600px;top:314px;width:54px;height:104px" role="img" aria-label="Pink silhouette of a girl jumping"></div>
</section>

<section class="card card--front">
  <svg class="swoosh" viewBox="0 0 704 170" aria-hidden="true">
    <defs>
      <linearGradient id="silverFront" x1="0" x2="1">
        <stop offset="0" stop-color="#a7a9ac"/><stop offset=".5" stop-color="#f2f2f4"/><stop offset="1" stop-color="#a7a9ac"/>
      </linearGradient>
    </defs>
    <path d="M704 0H0V140C90 80 230 36 380 26C510 18 630 30 704 42Z" fill="var(--red)"/>
    <path d="M380 26C240 36 90 90 0 132V92C90 60 230 30 380 26Z" fill="var(--royal)"/>
    <path d="M40 150C140 80 300 38 440 30C560 24 650 34 704 46" fill="none" stroke="url(#silverFront)" stroke-width="10"/>
  </svg>
  <div class="brand">
    <span class="brand__name">Marisol's Footlight Flyers</span>
    <span class="brand__tag">Drama Dance Performance and Fitness Studio</span>
  </div>
  <div class="figure figure--dancer" style="left:14px;top:132px;width:152px;height:210px" role="img" aria-label="Pink and purple silhouette of an adult dancing"></div>
  <div class="figure figure--sky" style="left:204px;top:226px;width:58px;height:116px" role="img" aria-label="Blue silhouette of a child with arms raised"></div>
  <div class="figure figure--pink" style="left:292px;top:248px;width:144px;height:72px" role="img" aria-label="Pink silhouette of a child doing a split jump"></div>
  <div class="figure figure--orange" style="left:496px;top:220px;width:58px;height:114px" role="img" aria-label="Orange silhouette of a child jumping"></div>
  <div class="figure figure--lime" style="left:606px;top:226px;width:70px;height:114px" role="img" aria-label="Green silhouette of a child star-jumping"></div>
  <div class="slogan">"Building Brave Hearts" - It's your turn to GLOW!</div>
</section>

</body>
</html>
```